Flyer Design Project

We are a mortgage company Bramwell Lending Corp. that will be looking to mail out these flyers to promote Reverse Mortgages. Some clip art of Seniors (Happy Smile having a good time) Our phone number on the flyer in a few places 877-260-5718
Text: No Celebrity Endorsers or talking heads here
Solutions for seniors... Stop worrying Start Living
Say Goodby to monthly payments with a reverse mortgage
The Loan That Pays You
Secure Your Retirement With A Reverse Mortgage
NLB Goverment Insured
Retain Complete ownership of your Home
Save and Effective Financial Tool
Pay Off Credit cards Elimanate Mortgage payments improve your home or lifestyle
No Credit score or income requirements
Faceing a foreclosure a reverse mortgage can help
Is a reverse mortgage right for you? Get the facts from a qualified reverse mortgage originator
The text above does not have to be in that order
I am having trouble with my Logo so i am getting a new file and will be able to upload it to the flyer shortly just leave room for it
Seniors over the age of 62
Financial

```html
<!DOCTYPE html>
<html lang="en">
<head>
<meta charset="utf-8">
<title>Bramwell Lending Corp. – Reverse Mortgage Flyer</title>
<link rel="stylesheet" href="https://fonts.googleapis.com/css2?family=Abril+Fatface&family=Arimo:wght@400;700&family=Questrial&display=swap">
<style>
  :root {
    --backdrop: #d9dcd8;
    --paper: #ffffff;
    --green-dark: #0f7a35;
    --green-text: #1b6e34;
    --lime: #a6c83a;
    --lime-pale: #e3efbf;
    --sky: #4d8ed8;
    --brick: #8a3a34;
    --title-panel: rgba(255,255,255,0.88);
  }
  * { box-sizing: border-box; margin: 0; padding: 0; }
  html, body { width: 1200px; height: 1200px; overflow: hidden; }
  body { background: var(--backdrop); position: relative; font-family: "Arimo", Arial, sans-serif; }

  .flyer {
    position: absolute; left: 285px; top: 40px;
    width: 630px; height: 1120px;
    background: var(--paper);
    overflow: hidden;
    box-shadow: 0 6px 24px rgba(0,0,0,0.18);
  }
  .flyer__photo {
    position: absolute; left: 0; top: 0; width: 630px; height: 558px;
    background: linear-gradient(180deg, var(--sky) 0%, #7fb0e6 30%, var(--brick) 55%, #a85a4c 80%, #7aa24a 100%);
  }
  .flyer__shapes { position: absolute; left: 0; top: 0; width: 630px; height: 1120px; }

  .brand-panel {
    position: absolute; left: 315px; top: 125px; width: 315px; height: 117px;
    background: var(--title-panel);
    display: flex; flex-direction: column; justify-content: center; padding-left: 18px;
    font-family: "Questrial", sans-serif; color: var(--green-dark);
    font-size: 34px; line-height: 44px; letter-spacing: 0.5px; white-space: nowrap;
  }

  .event { position: absolute; right: 30px; top: 618px; text-align: right; color: var(--green-dark); }
  .event__label { font-family: "Arimo", sans-serif; font-size: 21px; }
  .event__date { font-family: "Abril Fatface", serif; font-size: 40px; margin-top: 4px; }

  .benefits {
    position: absolute; left: 17px; top: 650px; width: 262px;
    list-style: none; color: var(--green-text);
    font-size: 11px; line-height: 16.5px;
  }

  .divider {
    position: absolute; left: 17px; top: 944px; width: 245px;
    border-top: 2px dotted var(--lime);
  }

  .contact { position: absolute; left: 17px; top: 962px; color: var(--green-text); font-size: 11.5px; line-height: 18px; }
  .contact__row { display: flex; gap: 18px; }
  .contact__item { display: flex; align-items: center; gap: 6px; }
  .contact__item::before {
    content: ""; width: 7px; height: 7px; background: var(--lime); flex: none;
  }
  .contact__address { margin-top: 6px; }
  .contact__address span { display: block; padding-left: 13px; }

  .logo-spot {
    position: absolute; left: 395px; top: 876px; width: 184px; height: 184px;
    border-radius: 50%; background: var(--paper);
    border: 6px solid var(--green-dark);
    box-shadow: 0 0 0 5px var(--lime-pale);
    display: flex; align-items: center; justify-content: center; text-align: center;
    font-family: "Arimo", sans-serif; font-size: 21px; color: var(--green-dark); line-height: 26px;
  }

  .footer-band {
    position: absolute; left: 0; bottom: 0; width: 630px; height: 48px; background: var(--green-dark);
  }
  .footer-stripe {
    position: absolute; left: 0; bottom: 48px; width: 630px; height: 4px; background: var(--lime);
  }
</style>
</head>
<body>
  <article class="flyer">
    <div class="flyer__photo" role="img" aria-label="Photo of a smiling family of four standing in front of a red brick house under a blue sky"></div>

    <svg class="flyer__shapes" viewBox="0 0 630 1120" aria-hidden="true">
      <polygon points="0,392 0,420 205,558 250,558" fill="var(--lime)"/>
      <polygon points="0,420 0,558 205,558" fill="var(--green-dark)"/>
      <polygon points="150,558 630,558 630,1000" fill="var(--lime-pale)"/>
      <polygon points="185,558 630,558 630,960" fill="var(--lime)"/>
    </svg>

    <div class="brand-panel">
      <span>BRAMWELL</span>
      <span>LENDING CORP</span>
    </div>

    <div class="event">
      <div class="event__label">Mortgage Application</div>
      <div class="event__date">01 September</div>
    </div>

    <ul class="benefits">
      <li>No Celebrity Endorsers or talking heads here</li>
      <li>Solutions for seniors... Stop worrying Start Living</li>
      <li>Say Goodby to monthly payments with a reverse mortgage</li>
      <li>The Loan That Pays You</li>
      <li>Secure Your Retirement With A Reverse Mortgage</li>
      <li>NLB Goverment Insured</li>
      <li>Retain Complete ownership of your Home</li>
      <li>Save and Effective Financial Tool</li>
      <li>Pay Off Credit cards Elimanate Mortgage payments improve your home or lifestyle</li>
      <li>No Credit score or income requirements</li>
      <li>Faceing a foreclosure a reverse mortgage can help</li>
      <li>Is a reverse mortgage right for you? Get the facts from a qualified reverse mortgage originator</li>
    </ul>

    <div class="divider"></div>

    <div class="contact">
      <div class="contact__row">
        <span class="contact__item">877-260-5718</span>
        <span class="contact__item">yourmail@domain.com</span>
      </div>
      <div class="contact__row">
        <span class="contact__item">111-222-4444</span>
        <span class="contact__item">www.yourwebsite.com</span>
      </div>
      <div class="contact__address">
        <div class="contact__item">Address: Street/Road Name/No</div>
        <span>Post Code City, Country Put Here</span>
      </div>
    </div>

    <div class="logo-spot">Bramwell<br>Lending</div>

    <div class="footer-stripe"></div>
    <div class="footer-band"></div>
  </article>
</body>
</html>
```